Country House in Italy Needs a Business Card Design

We need a business card design for “Casale del Ginepro”, a modern concept of a Farm Holidays/Country House to be opened in central Italy.
Attached is the company logo you did for us in the past.
Please
- create a double-sided business card design
- on the back I would like to have the logo
- on the front the copy
Copy on card:
o Casale del Ginepro
o Address: Via Pontemurra, 14
Cingoli (MC), Italy
o Website: www.casaledelginepro.it
o Email: info@casaledelginepro.it
o my name : Marisa
o my mobile phone number: +39 347 8123905
In the distribution of information keep in mind the possible inclusion also of a landline telephone number (currently not available / existing).
WE WOULD LIKE TO HAVE A MODERN, PROFFESIONAL, OUT OF THE BOX BUSINESS CARD. BE AS CREATIVE AS YOU WOULD LIKE.

```html
<!DOCTYPE html>
<html lang="it">
<head>
<meta charset="utf-8">
<title>Casale del Ginepro — Business Card</title>
<link rel="stylesheet" href="https://fonts.googleapis.com/css2?family=EB+Garamond:wght@400&family=Lato:wght@400&display=swap">
<style>
  :root {
    --page-bg: #e6e4e1;
    --orange-light: #f7a33f;
    --orange-mid: #ef8424;
    --orange-deep: #e2691a;
    --brown-text: #5a3620;
    --brown-motif: #6e4526;
    --cream: #f1ede6;
    --cream-shade: #e4ddd2;
    --accent-orange: #ee8a2c;
    --card-shadow: rgba(40, 30, 20, 0.28);
  }
  * { box-sizing: border-box; margin: 0; padding: 0; }
  html, body { width: 1200px; height: 1023px; overflow: hidden; }
  body { background: var(--page-bg); position: relative; }

  .card {
    position: absolute;
    width: 600px;
    height: 345px;
    border-radius: 4px;
    overflow: hidden;
    box-shadow: 0 14px 30px var(--card-shadow);
  }

  /* Front: contact copy */
  .card-front {
    left: 60px;
    top: 140px;
    background: linear-gradient(150deg, var(--orange-deep) 0%, var(--orange-mid) 40%, var(--orange-light) 70%, var(--orange-mid) 100%);
  }
  .front-motif {
    position: absolute;
    left: -150px;
    bottom: -190px;
    width: 400px;
    height: 400px;
    border-radius: 50%;
    background: radial-gradient(circle, rgba(110,69,38,0.55) 0%, rgba(110,69,38,0.9) 55%, rgba(110,69,38,0.35) 100%);
  }
  .front-copy {
    position: absolute;
    left: 300px;
    top: 34px;
    font-family: "EB Garamond", Georgia, serif;
    color: var(--brown-text);
  }
  .person-name { font-size: 30px; line-height: 1.1; margin-bottom: 8px; }
  .contact-line { font-size: 17px; line-height: 1.45; }
  .company-block { margin-top: 30px; }
  .company-name { font-size: 30px; line-height: 1.1; margin-bottom: 8px; }
  .address-line { font-size: 17px; line-height: 1.45; }

  /* Back: name mark */
  .card-back {
    left: 540px;
    top: 540px;
    background: radial-gradient(ellipse at 45% 40%, var(--cream) 0%, var(--cream) 55%, var(--cream-shade) 100%);
  }
  .brand-mark {
    position: absolute;
    left: 0;
    right: 0;
    top: 100px;
    text-align: center;
  }
  .brand-dot {
    display: block;
    width: 26px;
    height: 26px;
    margin: 0 auto 22px;
    border-radius: 50%;
    background: var(--accent-orange);
  }
  .brand-name {
    font-family: "EB Garamond", Georgia, serif;
    font-size: 52px;
    line-height: 1;
    color: var(--brown-text);
  }
  .brand-tagline {
    margin-top: 10px;
    font-family: "Lato", Arial, sans-serif;
    font-size: 22px;
    letter-spacing: 1px;
    color: var(--accent-orange);
    text-transform: uppercase;
  }
</style>
</head>
<body>
  <section class="card card-front">
    <div class="front-motif" role="img" aria-label="Brown mosaic rosette pattern in the lower left corner"></div>
    <div class="front-copy">
      <p class="person-name">Marisa</p>
      <p class="contact-line">+39 347 8123905</p>
      <p class="contact-line">info@casaledelginepro.it</p>
      <p class="contact-line">www.casaledelginepro.it</p>
      <div class="company-block">
        <p class="company-name">Casale del Ginepro</p>
        <p class="address-line">Via Pontemurra, 14</p>
        <p class="address-line">62100 Valdaspro</p>
        <p class="address-line">(MC), Italy</p>
      </div>
    </div>
  </section>

  <section class="card card-back" role="img" aria-label="Card back with faint cream mosaic pattern and the company name">
    <div class="brand-mark">
      <span class="brand-dot"></span>
      <p class="brand-name">Casale del Ginepro</p>
      <p class="brand-tagline">Country House</p>
    </div>
  </section>
</body>
</html>
```